Business Card Design Project

We consult with hotels on setting rates and maximizing a revenue strategy

Industry/Entity Type

Business

Contact Information for Business Card

I am not sure what I want. Our company offers high level consulting to hotels around the country but we are also laid back. I would like something that is professional but also shows the laid back side

```html
<!DOCTYPE html>
<html lang="en">
<head>
<meta charset="utf-8">
<title>Harborline Business Card</title>
<link href="https://fonts.googleapis.com/css2?family=Montserrat:wght@400;500;700;800&family=Didact+Gothic&display=swap" rel="stylesheet">
<style>
  :root {
    --stage: #2b2b2d;
    --brown: #3b261f;
    --teal: #1f6f66;
    --teal-light: #5fb3a8;
    --ink: #2a1c17;
    --paper: #ffffff;
    --rule: #3b261f;
  }
  * { box-sizing: border-box; margin: 0; padding: 0; }
  html, body { width: 1200px; height: 900px; overflow: hidden; }
  body {
    background: var(--stage);
    font-family: "Montserrat", sans-serif;
    position: relative;
  }
  .card {
    position: absolute;
    left: 260px;
    width: 680px;
    height: 388px;
    border-radius: 22px;
    overflow: hidden;
    box-shadow: 0 18px 40px rgba(0,0,0,0.45);
  }

  /* Front */
  .card-front { top: 50px; background: var(--brown); color: var(--paper); }
  .front-brand {
    position: absolute;
    left: 290px;
    right: 36px;
    top: 120px;
  }
  .front-name {
    font-weight: 700;
    font-size: 40px;
    letter-spacing: 1px;
    line-height: 1;
    display: flex;
    align-items: center;
    gap: 10px;
    white-space: nowrap;
  }
  .brand-mark { width: 16px; height: 16px; background: var(--teal-light); display: inline-block; flex: none; }
  .front-tagline { font-weight: 700; font-size: 19px; margin-top: 10px; white-space: nowrap; }
  .front-web { font-family: "Didact Gothic", sans-serif; font-size: 22px; margin-top: 10px; letter-spacing: 0.5px; white-space: nowrap; }

  /* Back */
  .card-back { top: 482px; background: var(--paper); color: var(--ink); }
  .back-brand {
    position: absolute;
    left: 44px;
    top: 120px;
    display: flex;
    align-items: center;
    gap: 10px;
  }
  .back-brand .brand-mark { width: 16px; height: 16px; background: var(--teal); }
  .back-brand-text .name { font-weight: 700; font-size: 34px; letter-spacing: 1.5px; color: var(--brown); line-height: 1; white-space: nowrap; }
  .back-brand-text .tagline {
    margin-top: 4px;
    background: var(--brown);
    color: var(--paper);
    font-weight: 700;
    font-size: 11px;
    padding: 2px 8px;
    display: inline-block;
    white-space: nowrap;
  }
  .person {
    position: absolute;
    right: 40px;
    top: 92px;
    text-align: right;
  }
  .person-name { font-weight: 800; font-size: 32px; letter-spacing: 2px; color: var(--ink); padding-bottom: 6px; border-bottom: 2px solid var(--rule); white-space: nowrap; }
  .person-title { font-family: "Didact Gothic", sans-serif; font-size: 19px; color: var(--teal); margin-top: 4px; white-space: nowrap; }

  .contact-rule { position: absolute; left: 40px; top: 250px; width: 360px; height: 1.5px; background: var(--rule); }
  .contacts { position: absolute; left: 40px; top: 258px; list-style: none; }
  .contacts li {
    display: flex; align-items: center; gap: 12px;
    font-family: "Didact Gothic", sans-serif;
    font-size: 19px; color: var(--teal); line-height: 24px;
    white-space: nowrap;
  }
  .contacts svg { width: 14px; height: 14px; fill: var(--brown); flex: none; }
  .back-bands { position: absolute; left: 0; bottom: 0; width: 680px; height: 90px; }
  .band-brown { fill: var(--brown); }
  .band-teal { fill: var(--teal); }
</style>
</head>
<body>

<section class="card card-front" aria-label="Card front">
  <div class="front-brand">
    <div class="front-name"><span class="brand-mark"></span>HARBORLINE</div>
    <div class="front-tagline">Revenue Management Solutions</div>
    <div class="front-web">www.HarborlineRMS.com</div>
  </div>
</section>

<section class="card card-back" aria-label="Card back">
  <div class="back-brand">
    <span class="brand-mark"></span>
    <div class="back-brand-text">
      <div class="name">HARBORLINE</div>
      <div class="tagline">Revenue Management Solutions</div>
    </div>
  </div>

  <div class="person">
    <div class="person-name">MAREN HOLT</div>
    <div class="person-title">Regional Revenue Manager</div>
  </div>

  <div class="contact-rule"></div>
  <ul class="contacts">
    <li><svg viewBox="0 0 16 16"><path d="M3 1l3 3-2 2c1 2 3 4 5 5l2-2 3 3-2 3C6 15 1 10 1 3z"/></svg>503-555-0142</li>
    <li><svg viewBox="0 0 16 16"><rect x="4" y="1" width="8" height="14" rx="1.5"/></svg>503-555-0187</li>
    <li><svg viewBox="0 0 16 16"><path d="M1 3h14v10H1z M1 3l7 6 7-6" fill="none" stroke="#3b261f" stroke-width="1.6"/></svg>Maren@HarborlineRMS.com</li>
    <li><svg viewBox="0 0 16 16"><circle cx="8" cy="8" r="6.5" fill="none" stroke="#3b261f" stroke-width="1.5"/><path d="M1.5 8h13M8 1.5c-3 3-3 10 0 13M8 1.5c3 3 3 10 0 13" fill="none" stroke="#3b261f" stroke-width="1.2"/></svg>www.HarborlineRMS.com</li>
  </ul>

  <svg class="back-bands" viewBox="0 0 680 90" preserveAspectRatio="none" aria-hidden="true">
    <polygon class="band-brown" points="0,82 680,42 680,90 0,90"/>
    <polygon class="band-teal" points="520,14 680,0 680,90 505,90 505,60"/>
  </svg>
</section>

</body>
</html>
```